I need a design with just the number 24. must be in blue color (royal blue) should be large enough for people see must be in the center of page. Place a nice border around the page.

Requirements
Must have
• Number 24 in Royal blue color

```html
<!DOCTYPE html>
<html lang="en">
<head>
<meta charset="UTF-8">
<title>Number 24 Signs</title>
<link href="https://fonts.googleapis.com/css2?family=Anton&display=swap" rel="stylesheet">
<style>
  :root {
    --backdrop: #333333;
    --royal-blue: #0000ff;
    --paper: #ffffff;
  }
  html, body {
    margin: 0;
    padding: 0;
    width: 1200px;
    height: 848px;
    overflow: hidden;
    background: var(--backdrop);
  }
  .sign-sheet {
    display: block;
    width: 1200px;
    height: 848px;
  }
  .sheet-backdrop { fill: var(--backdrop); }
  .sign-solid-frame { fill: var(--royal-blue); }
  .sign-paper { fill: var(--paper); }
  .sign-line-frame {
    fill: none;
    stroke: var(--royal-blue);
    stroke-width: 8;
  }
  .house-number {
    font-family: "Anton", "Oswald", Impact, sans-serif;
    font-size: 446px;
    fill: var(--royal-blue);
  }
</style>
</head>
<body>
<svg class="sign-sheet" viewBox="0 0 1200 848" xmlns="http://www.w3.org/2000/svg">
  <rect class="sheet-backdrop" x="0" y="0" width="1200" height="848"/>

  <g class="sign sign--solid-border">
    <rect class="sign-solid-frame" x="66" y="74" width="476" height="698"/>
    <rect class="sign-paper" x="91" y="101" width="426" height="644" rx="7"/>
    <text class="house-number" x="304" y="578" text-anchor="middle"
          textLength="338" lengthAdjust="spacingAndGlyphs">24</text>
  </g>

  <g class="sign sign--line-border">
    <rect class="sign-paper" x="604" y="74" width="476" height="698"/>
    <rect class="sign-line-frame" x="625" y="96.5" width="420" height="652.5" rx="15"/>
    <text class="house-number" x="842" y="578" text-anchor="middle"
          textLength="338" lengthAdjust="spacingAndGlyphs">24</text>
  </g>
</svg>
</body>
</html>
```